Modern Lawfirm Business Card Design

We're looking for a business card to incorporate the newly created logo we had made.

Ideally looking for a law firm business card demonstrating, modern, minimalist, strong/bold design.

I'm open to any design honestly, but nothing "flashy".

Target Market(s)

Immigration law, family immigration, humanitarian, general legal

Industry/Entity Type

Law Firm

Contact Information for Business Card

Please use dummy information, name, street address, city, state, phone number, email, website.

Font styles to use
Serif
Sans Serif

Requirements
Must have
• Please use dummy information, name, street address, city, state, phone number, email, website.

```html
<!DOCTYPE html>
<html lang="en">
<head>
<meta charset="utf-8">
<title>Valcarce Immigration Law — Business Card</title>
<link rel="stylesheet" href="https://fonts.googleapis.com/css2?family=Tinos:wght@400&display=swap">
<style>
  :root {
    --firm-blue: #0a5ba3;
    --card-white: #ffffff;
    --stage: #d4d4d4;
    --ink-light: #ffffff;
  }
  * { margin: 0; padding: 0; box-sizing: border-box; }
  html, body {
    width: 1200px; height: 1200px; overflow: hidden;
    background: var(--stage);
    font-family: "Tinos", "Times New Roman", serif;
    font-weight: 400;
  }
  .canvas { position: relative; width: 1200px; height: 1200px; }
  .card {
    position: absolute; left: 377px;
    width: 446px; height: 254px;
    background: var(--card-white);
    overflow: hidden;
  }
  .card--front { top: 216px; }
  .card--back { top: 672px; }

  .firm-name {
    position: absolute; left: 0; right: 0;
    display: flex; align-items: center; justify-content: center; gap: 8px;
    color: var(--firm-blue);
    white-space: nowrap; line-height: 1;
  }
  .firm-name__mark { flex: none; background: var(--firm-blue); }
  .card--front .firm-name { top: 113px; font-size: 24px; }
  .card--front .firm-name__mark { width: 16px; height: 16px; }
  .card--back .firm-name { top: 63px; font-size: 17px; }
  .card--back .firm-name__mark { width: 11px; height: 11px; }

  .contact-band {
    position: absolute; left: 0; right: 0; bottom: 0; height: 127px;
    background: var(--firm-blue);
    color: var(--ink-light);
  }
  .holder { position: absolute; left: 0; right: 0; top: 19px; text-align: center; }
  .holder__name { font-size: 22px; line-height: 1; }
  .holder__title { font-size: 9px; line-height: 1; margin-top: 3px; }

  .contact-list { list-style: none; position: absolute; top: 65px; font-size: 11px; line-height: 12.5px; }
  .contact-list--left { left: 42px; }
  .contact-list--right { left: 245px; }
  .contact-list li { display: flex; align-items: flex-start; gap: 8px; }
  .contact-list svg { width: 7px; height: 7px; margin-top: 3px; flex: none; fill: var(--ink-light); }
</style>
</head>
<body>
<main class="canvas">
  <section class="card card--front">
    <p class="firm-name"><span class="firm-name__mark"></span>Valcarce Immigration Law</p>
  </section>

  <section class="card card--back">
    <p class="firm-name"><span class="firm-name__mark"></span>Valcarce Immigration Law</p>
    <div class="contact-band">
      <div class="holder">
        <p class="holder__name">Your Name</p>
        <p class="holder__title">Your Tittle</p>
      </div>
      <ul class="contact-list contact-list--left">
        <li>
          <svg viewBox="0 0 10 10" aria-hidden="true"><path d="M5 0a3.5 3.5 0 0 0-3.5 3.5C1.5 6 5 10 5 10s3.5-4 3.5-6.5A3.5 3.5 0 0 0 5 0zm0 5a1.4 1.4 0 1 1 0-2.8A1.4 1.4 0 0 1 5 5z"/></svg>
          <span>2280 N. Harwood Street Suite<br>410 Dallas, TX 75201</span>
        </li>
        <li>
          <svg viewBox="0 0 10 10" aria-hidden="true"><path d="M2 0l2 2.5-1.2 1.3a6 6 0 0 0 3.4 3.4L7.5 6 10 8 8.6 9.6C4.5 10 0 5.5.4 1.4z"/></svg>
          <span>(214) 555-0148</span>
        </li>
      </ul>
      <ul class="contact-list contact-list--right">
        <li>
          <svg viewBox="0 0 10 10" aria-hidden="true"><path d="M0 2h10v6H0z"/></svg>
          <span>info@valcarceimmigrationlaw.com</span>
        </li>
        <li>
          <svg viewBox="0 0 10 10" aria-hidden="true"><circle cx="5" cy="5" r="4.5"/></svg>
          <span>www.valcarceimmigrationlaw.com</span>
        </li>
      </ul>
    </div>
  </section>
</main>
</body>
</html>
```